Restaurant service company needs a website!

I am looking for a skilled web designer/developer to create a professional, responsive, and easy-to-navigate website for my company, which specializes in servicing restaurant cooking equipment. The site should communicate trust, reliability, and technical expertise to our target audience, restaurant owners, managers, and commercial kitchen operators. I have included the company logos, if any other format for them is needed please let me know.

Target Market(s)

restaurant owners, managers, and commercial kitchen operators

Industry/Entity Type

Commercial Kitchen Equipment Service

Coding

Coded - Design and coding required

Number of Pages Required

1 page

Font styles to use
Serif
Sans Serif

Requirements
Must have
• Contact and service request forms, Click-to-call functionality for mobile, Clean, modern layout with strong visuals, Easy navigation, mobile-friendly
Nice to have
• Testimonials or Reviews, If possible a click-to-text functionality for mobile.
Should not have
• Any mention of Refrigeration or HVAC, "Free Quotes"

```html
<!DOCTYPE html>
<html lang="en">
<head>
<meta charset="utf-8">
<title>Waypoint Kitchen Service</title>
<link href="https://fonts.googleapis.com/css2?family=Outfit:wght@400;500;600;700&display=swap" rel="stylesheet">
<style>
:root{
  --teal:#0a6584;
  --teal-dark:#0b4f6b;
  --ink:#14384a;
  --text:#2b3f4a;
  --muted:#5d6e77;
  --field:#f1f5f6;
  --card:#e9eff2;
  --sky:#e0f3f8;
  --star:#f0a22c;
  --white:#ffffff;
}
*{box-sizing:border-box;margin:0;padding:0}
html,body{width:1200px;height:3916px;overflow:hidden}
body{font-family:"Outfit",Arial,sans-serif;color:var(--text);background:var(--white);position:relative}
.abs{position:absolute}
a{color:inherit;text-decoration:none}
.btn{position:absolute;display:flex;align-items:center;justify-content:center;font-size:12px;font-weight:600;border-radius:3px}
.btn-solid{background:var(--teal);color:#fff;clip-path:polygon(0 0,88% 0,100% 40%,100% 100%,0 100%)}
.btn-ghost{border:1.5px solid var(--teal);color:var(--teal);background:#fff}
.btn-ghost-light{border:1.5px solid #fff;color:#fff}

/* header */
.site-header{position:absolute;left:0;top:0;width:1200px;height:69px;background:#fff}
.brand{position:absolute;left:94px;top:14px;display:flex;align-items:center;gap:8px}
.brand-dot{width:28px;height:28px;border:2px solid var(--teal);border-radius:4px}
.brand-name{font-size:20px;font-weight:600;color:var(--teal);line-height:1}
.main-nav{position:absolute;left:388px;top:27px;display:flex;gap:25px;font-size:12px;color:#2d3b44}
.nav-home{width:12px;height:12px}

/* hero */
.hero{position:absolute;left:0;top:69px;width:1200px;height:678px;overflow:hidden}
.hero-photo{position:absolute;inset:0;background:linear-gradient(100deg,#1d1b19 0%,#3b3530 35%,#6d665d 60%,#8c8a86 80%,#a8aaa8 100%)}
.hero-shade{position:absolute;inset:0;background:linear-gradient(90deg,rgba(0,0,0,.55),rgba(0,0,0,.1) 60%,rgba(0,0,0,0))}
.hero h1{position:absolute;left:94px;top:240px;width:600px;font-size:38px;line-height:46px;font-weight:600;color:#fff}
.hero-lead{position:absolute;left:94px;top:342px;width:460px;font-size:13px;line-height:18px;color:#fff}

.request-card{position:absolute;left:747px;top:94px;width:319px;height:491px;background:#fff;border-radius:10px;clip-path:polygon(0 0,82% 0,100% 9%,100% 100%,0 100%)}
.request-card h2{position:absolute;left:31px;top:38px;font-size:18px;font-weight:600;color:var(--ink)}
.field{position:absolute;left:31px;width:261px;height:32px;background:var(--field);border-radius:3px;font-size:11px;color:#3a4a52;padding:10px 18px}
.field-notes{height:97px}
.card-note{position:absolute;left:31px;top:424px;width:220px;font-size:9px;line-height:14px;color:#3a4a52}

/* about */
.photo{position:absolute;border-radius:8px}
.about-tag{position:absolute;left:639px;top:903px;font-size:12px;color:var(--teal)}
.about-title{position:absolute;left:639px;top:922px;font-size:29px;line-height:36px;font-weight:600;color:var(--ink)}
.about-copy{position:absolute;left:639px;top:1000px;width:450px;font-size:11.5px;line-height:17px;color:#2d3b44}
.feature{position:absolute;left:636px;display:flex;gap:12px;align-items:center}
.feature-icon{width:50px;height:50px;flex:none}
.feature h3{font-size:14px;font-weight:600;color:var(--ink)}
.feature p{font-size:11.5px;color:#2d3b44;margin-top:2px}

/* services */
.section-title{position:absolute;left:0;width:1200px;text-align:center;font-weight:600;color:var(--ink)}
.section-title span{display:inline-block;width:42px;height:4px;border-radius:2px;background:var(--teal);vertical-align:middle;margin:0 10px}
.section-sub{position:absolute;left:0;width:1200px;text-align:center;font-size:12px;color:#2d3b44}
.service-card{position:absolute;top:1471px;width:245px;height:346px;border-radius:10px;overflow:hidden;clip-path:polygon(0 0,80% 0,100% 14%,100% 100%,0 100%)}
.service-card.light{background:var(--card)}
.service-card .shade{position:absolute;inset:0;background:linear-gradient(180deg,rgba(0,0,0,0) 45%,rgba(0,0,0,.75))}
.service-card h3{position:absolute;left:36px;bottom:33px;font-size:18px;line-height:22px;font-weight:600;color:#fff}
.service-card.light h3{color:var(--ink);bottom:auto;top:216px}
.service-card .desc{position:absolute;left:36px;top:247px;width:148px;font-size:11px;line-height:14px;color:#2d3b44}
.service-card .more{position:absolute;left:36px;top:300px;font-size:11px;font-weight:600;color:var(--teal);text-decoration:underline}

/* industries */
.industries{position:absolute;left:0;top:2027px;width:1200px;height:527px;border-radius:40px 40px 0 0;overflow:hidden;background:linear-gradient(90deg,#3a2e25,#6e5a48 35%,#b7aea4 65%,#7f7366 100%)}
.industry-card{position:absolute;left:94px;top:2152px;width:320px;height:272px;background:var(--teal);border-radius:10px;clip-path:polygon(0 0,86% 0,100% 15%,100% 100%,0 100%)}
.industry-card small{position:absolute;left:52px;top:72px;font-size:10px;color:#fff}
.industry-card h2{position:absolute;left:52px;top:92px;font-size:27px;line-height:30px;font-weight:600;color:#fff}
.round-btn{position:absolute;width:32px;height:32px;border-radius:50%;display:flex;align-items:center;justify-content:center;font-size:13px;color:#fff}

/* testimonials */
.testimonials{position:absolute;left:0;top:2554px;width:1200px;height:558px;background:var(--sky);border-radius:0 0 40px 40px}
.quote-mark{position:absolute;left:205px;top:2680px;font-size:150px;line-height:120px;font-weight:700;color:var(--teal-dark);height:80px;overflow:hidden}
.testimonials-title{position:absolute;left:205px;top:2763px;font-size:30px;font-weight:600;color:var(--ink)}
.testimonial-quote{position:absolute;left:205px;top:2808px;width:340px;font-size:19px;line-height:24px;color:#223742}
.reviewer{position:absolute;left:205px;top:2890px;font-size:13px;font-weight:500;color:#1b2e38}
.stars{position:absolute;left:204px;top:2907px;color:var(--star);font-size:15px;letter-spacing:1px}
.avatar{position:absolute;border-radius:50%;border:3px solid #fff;background:linear-gradient(135deg,#c7b8aa,#8a9aa4)}

/* cta */
.cta-icon{position:absolute;left:565px;top:3206px;width:70px;height:70px}
.cta-buttons .btn{top:3363px}

/* footer */
.site-footer{position:absolute;left:0;top:3506px;width:1200px;height:410px;background:var(--teal);border-radius:40px 40px 0 0;overflow:hidden;color:#fff}
.footer-frame{position:absolute;left:38px;top:38px;width:1124px;height:420px;border:26px solid rgba(255,255,255,.06);border-radius:60px}
.footer-brand{position:absolute;left:140px;top:160px;width:186px;text-align:center}
.footer-brand .mark{width:70px;height:70px;margin:0 auto 12px;border:4px solid #fff;border-radius:50%}
.footer-brand b{display:block;font-size:20px;font-weight:600}
.footer-brand i{display:block;font-style:normal;font-size:9px;letter-spacing:3px;margin-top:2px}
.footer-col{position:absolute;top:160px;font-size:12px;line-height:20px}
.footer-col h4{font-size:16px;font-weight:600;margin-bottom:8px}
.socials{display:flex;gap:8px}
.socials span{width:30px;height:30px;border-radius:50%;background:rgba(255,255,255,.15)}
.footer-rule{position:absolute;left:94px;top:364px;width:1012px;height:1px;background:rgba(255,255,255,.3)}
.copyright{position:absolute;left:0;top:382px;width:1200px;text-align:center;font-size:11px}
.to-top{position:absolute;left:1120px;top:344px;width:32px;height:32px;border-radius:50%;background:#fff;color:var(--teal);display:flex;align-items:center;justify-content:center;font-size:12px}
</style>
</head>
<body>

<header class="site-header">
  <div class="brand"><span class="brand-dot"></span><span class="brand-name">WAYPOINT</span></div>
  <nav class="main-nav">
    <svg class="nav-home" viewBox="0 0 12 12"><path d="M1 6 6 1l5 5H9.5v5h-7V6z" fill="#0a6584"/></svg>
    <a>About Us</a><a>Services</a><a>Industries Served</a><a>Testimonials</a><a>Contact</a>
  </nav>
  <a class="btn btn-solid" style="left:984px;top:18px;width:122px;height:32px">Request Service</a>
</header>

<section class="hero">
  <div class="hero-photo" role="img" aria-label="Chefs working at a commercial kitchen range"></div>
  <div class="hero-shade"></div>
  <h1>Reliable Service for Your Restaurant Cooking Equipment</h1>
  <p class="hero-lead">We keep your commercial kitchen running smoothly with trusted repairs, expert maintenance, and fast response times.</p>
  <a class="btn btn-solid" style="left:94px;top:392px;width:122px;height:30px">Request Service</a>
  <a class="btn btn-ghost-light" style="left:222px;top:392px;width:119px;height:30px">Call Us Today</a>

  <form class="request-card">
    <h2>Request a Service Visit</h2>
    <div class="field" style="top:86px">Business Name</div>
    <div class="field" style="top:123px">Contact Person</div>
    <div class="field" style="top:161px">Phone</div>
    <div class="field" style="top:199px">Email</div>
    <div class="field" style="top:238px">Equipment Type</div>
    <div class="field field-notes" style="top:277px">Problem / Notes</div>
    <a class="btn btn-solid" style="left:31px;top:383px;width:106px;height:32px">Send Request</a>
    <a class="btn btn-ghost" style="left:140px;top:383px;width:85px;height:32px">Call Now</a>
    <p class="card-note">We will call to confirm scheduling. If this is an emergency, please use the Call Now button.</p>
  </form>
</section>

<section class="about">
  <div class="photo" style="left:96px;top:867px;width:199px;height:202px;background:linear-gradient(160deg,#d9dadb,#6b6f72)" role="img" aria-label="Gas range with a stock pot"></div>
  <div class="photo" style="left:96px;top:1078px;width:199px;height:186px;background:linear-gradient(160deg,#e4e6e7,#5c6166)" role="img" aria-label="Stainless steel kitchen line"></div>
  <div class="photo" style="left:307px;top:867px;width:281px;height:397px;background:linear-gradient(160deg,#b9bcbc,#3a3530 60%,#1f1d1b);clip-path:polygon(0 0,85% 0,100% 8%,100% 100%,0 100%)" role="img" aria-label="Chef cooking at a commercial range"></div>

  <p class="about-tag">About Us</p>
  <h2 class="about-title">Trusted Service.<br>Proven Expertise.</h2>
  <p class="about-copy">For years, we've been helping restaurants and commercial kitchens keep their equipment performing at its best. Our team of certified technicians specializes in servicing all major brands of cooking equipment. From emergency repairs to routine maintenance, we deliver professional service you can count on.</p>

  <div class="feature" style="top:1082px">
    <svg class="feature-icon" viewBox="0 0 50 50"><circle cx="25" cy="25" r="23" fill="none" stroke="#0a6584" stroke-dasharray="2 3"/><circle cx="25" cy="25" r="19" fill="#0a6584"/><path d="M17 25l5 5 11-11" stroke="#fff" stroke-width="2.5" fill="none"/></svg>
    <div><h3>Reliability</h3><p>We respond quickly and get the job done right.</p></div>
  </div>
  <div class="feature" style="top:1137px">
    <svg class="feature-icon" viewBox="0 0 50 50"><circle cx="25" cy="25" r="23" fill="none" stroke="#0a6584" stroke-dasharray="2 3"/><circle cx="25" cy="25" r="19" fill="#0a6584"/><circle cx="25" cy="20" r="4" fill="#fff"/><path d="M17 33c2-5 14-5 16 0z" fill="#fff"/></svg>
    <div><h3>Expertise</h3><p>Skilled technicians with hands-on industry knowledge.</p></div>
  </div>
  <div class="feature" style="top:1191px">
    <svg class="feature-icon" viewBox="0 0 50 50"><circle cx="25" cy="25" r="23" fill="none" stroke="#0a6584" stroke-dasharray="2 3"/><circle cx="25" cy="25" r="19" fill="#0a6584"/><path d="M25 14l8 3v7c0 6-4 9-8 11-4-2-8-5-8-11v-7z" fill="none" stroke="#fff" stroke-width="2"/><path d="M21 25l3 3 5-5" stroke="#fff" stroke-width="2" fill="none"/></svg>
    <div><h3>Trust</h3><p>Clear communication, honest pricing, and dependable results.</p></div>
  </div>
</section>

<section class="services">
  <h2 class="section-title" style="top:1380px;font-size:30px"><span></span>What We Do Best<span></span></h2>
  <p class="section-sub" style="top:1424px">We provide complete service solutions for restaurant cooking equipment:</p>

  <article class="service-card light" style="left:94px">
    <svg class="abs" style="left:36px;top:38px" width="62" height="62" viewBox="0 0 62 62"><circle cx="31" cy="31" r="29" fill="none" stroke="#0a6584" stroke-dasharray="2 3"/><circle cx="31" cy="31" r="24" fill="#0a6584"/><path d="M22 40l16-16M36 22l4 4M22 24l14 14" stroke="#fff" stroke-width="2.5" stroke-linecap="round"/></svg>
    <h3>Equipment Repair</h3>
    <p class="desc">Fast, reliable repairs for ovens, grills, fryers, ranges, and more.</p>
    <a class="more">Read More</a>
  </article>
  <article class="service-card" style="left:351px;background:linear-gradient(160deg,#c9c6c2,#5b4e44 60%,#2a2420)" role="img" aria-label="Cooks at a range during service">
    <div class="shade"></div><h3>Preventive<br>Maintenance</h3>
  </article>
  <article class="service-card" style="left:607px;background:linear-gradient(160deg,#d6d7d8,#6a6d70 55%,#2b2d30)" role="img" aria-label="Steel kitchen with kettle on the range">
    <div class="shade"></div><h3>Emergency<br>Service</h3>
  </article>
  <article class="service-card" style="left:861px;background:linear-gradient(160deg,#8d9296,#3a3c40 55%,#15171a)" role="img" aria-label="Newly installed commercial kitchen">
    <div class="shade"></div><h3>Installation<br>&amp; Setup</h3>
  </article>
</section>

<section class="industries" role="img" aria-label="Chef cooking in a busy restaurant kitchen"></section>
<div class="industry-card">
  <small>Industries We Serve</small>
  <h2>Restaurants<br>&amp; Cafés</h2>
  <span class="round-btn" style="left:52px;top:184px;background:var(--teal-dark)">‹</span>
  <span class="round-btn" style="left:92px;top:184px;background:rgba(255,255,255,.2)">›</span>
</div>

<section class="testimonials"></section>
<div class="quote-mark">“</div>
<h2 class="testimonials-title">What Our Clients Say</h2>
<blockquote class="testimonial-quote">They saved our kitchen during a busy weekend rush. Fast, professional, and dependable service.</blockquote>
<p class="reviewer">Restaurant Manager</p>
<p class="stars">★★★★★</p>
<span class="round-btn" style="left:205px;top:2945px;background:var(--teal-dark)">‹</span>
<span class="round-btn" style="left:244px;top:2945px;background:var(--teal-dark)">›</span>

<div class="abs" style="left:630px;top:2670px;width:342px;height:342px;border-radius:50%;background:radial-gradient(circle,#cfe8f0,#e0f3f8 70%)" role="img" aria-label="Portraits of satisfied clients"></div>
<div class="avatar" style="left:727px;top:2668px;width:38px;height:38px"></div>
<div class="avatar" style="left:624px;top:2745px;width:56px;height:56px"></div>
<div class="avatar" style="left:927px;top:2762px;width:38px;height:38px"></div>
<div class="avatar" style="left:766px;top:2808px;width:70px;height:70px"></div>
<div class="avatar" style="left:835px;top:2940px;width:56px;height:56px"></div>

<section class="cta">
  <svg class="cta-icon" viewBox="0 0 70 70"><circle cx="35" cy="35" r="33" fill="none" stroke="#0a6584" stroke-width="2"/><circle cx="30" cy="38" r="9" fill="none" stroke="#0a6584" stroke-width="2.5"/><circle cx="30" cy="38" r="3" fill="#0a6584"/><path d="M40 20l8 8M44 18l-6 16M46 34l-4 8" stroke="#0a6584" stroke-width="2.5" stroke-linecap="round"/></svg>
  <h2 class="section-title" style="top:3282px;font-size:30px"><span></span>Need Immediate Service?<span></span></h2>
  <p class="section-sub" style="top:3330px">We're just a call or click away. Request a technician today and keep your kitchen running at full speed.</p>
  <div class="cta-buttons">
    <a class="btn btn-solid" style="left:476px;width:122px;height:31px">Request Service</a>
    <a class="btn btn-ghost" style="left:603px;width:121px;height:31px">Call Us Today</a>
  </div>
</section>

<footer class="site-footer">
  <div class="footer-frame"></div>
  <div class="footer-brand"><div class="mark"></div><b>WAYPOINT</b><i>KITCHEN SERVICE</i></div>
  <div class="footer-col" style="left:429px"><h4>Quick Links</h4>Home<br>About Us<br>Services<br>Contact</div>
  <div class="footer-col" style="left:630px"><h4>Business Hours</h4>Mon–Fri: 8:00 AM – 8:00 PM<br>Sat: 9:00 AM – 5:00 PM<br>Emergency service available</div>
  <div class="footer-col" style="left:902px"><h4>Social Media</h4><div class="socials"><span></span><span></span><span></span><span></span></div></div>
  <div class="footer-rule"></div>
  <p class="copyright">Copyright © 2025 Waypoint Kitchen Service. All Rights Reserved.</p>
  <span class="to-top">˄</span>
</footer>

</body>
</html>
```